Quality spirits brand needs a bottle design and logo

Designs look the same

We have received 3 designs. The font options for both of these were good, and we liked them. However, the image used wasn't strong enough. we want an image that speaks strongly in black and white, to do that it needs to be simplified some with less fine detail. We would also like to ensure some space is left for the type of spirit in the bottle i.e. RUM, SPICED RUM, VODKA, GIN

Please read the brief we have posted with the project closely to ensure you get a good understanding of what we are after.

```html
<!DOCTYPE html>
<html lang="en">
<head>
<meta charset="utf-8">
<title>Wild Meridian – Spirit Bottle Range</title>
<link rel="stylesheet" href="https://fonts.googleapis.com/css2?family=Bebas+Neue&family=Montserrat:wght@300;400&family=Herr+Von+Muellerhoff&display=swap">
<style>
  :root {
    --paper: #ffffff;
    --ink: #111111;
    --ink-spiced: #2a1a10;
    --ink-muted: #4a4a4a;
    --glass: #eef0f3;
    --glass-edge: #c4c8cd;
    --cap: #161616;
    --cork: #d3c0a2;
    --amber-top: #d98a2a;
    --amber-bottom: #b0501a;
  }
  * { box-sizing: border-box; margin: 0; padding: 0; }
  html, body {
    width: 1200px;
    height: 1200px;
    overflow: hidden;
    background: var(--paper);
  }
  .bottle-range {
    position: relative;
    width: 1200px;
    height: 1200px;
  }
  .bottles {
    position: absolute;
    inset: 0;
  }
  .glass { fill: var(--glass); stroke: var(--glass-edge); stroke-width: 2; }
  .cap { fill: var(--cap); }
  .cork { fill: var(--cork); }

  .label {
    position: absolute;
    top: 0;
    width: 0;
    height: 1200px;
    color: var(--ink);
  }
  .label > * {
    position: absolute;
    left: 0;
    transform: translateX(-50%);
    white-space: nowrap;
    text-align: center;
    line-height: 1;
  }
  .label--white-rum { left: 231px; }
  .label--spiced-rum { left: 618px; color: var(--ink-spiced); }
  .label--vodka { left: 986px; }

  .brand-mark {
    border-radius: 50%;
    background: currentColor;
  }
  .brand-word {
    font-family: "Bebas Neue", sans-serif;
    font-weight: 400;
    transform: translateX(-50%) scaleY(1.5);
    transform-origin: top center;
    letter-spacing: 1px;
  }
  .brand-sub {
    font-family: "Bebas Neue", sans-serif;
    font-weight: 400;
    letter-spacing: 1px;
  }
  .tagline {
    font-family: "Herr Von Muellerhoff", cursive;
  }
  .spirit-type {
    font-family: "Montserrat", sans-serif;
    font-weight: 400;
    font-size: 18px;
    letter-spacing: 5px;
  }
  .specs {
    display: flex;
    justify-content: space-between;
    font-family: "Montserrat", sans-serif;
    font-weight: 300;
    font-size: 9px;
    color: var(--ink-muted);
  }

  /* White rum */
  .label--white-rum .brand-mark { top: 560px; width: 76px; height: 76px; }
  .label--white-rum .brand-word { top: 625px; font-size: 115px; }
  .label--white-rum .brand-sub { top: 766px; font-size: 60px; }
  .label--white-rum .tagline { top: 828px; font-size: 30px; }
  .label--white-rum .spirit-type { top: 881px; }
  .label--white-rum .specs { top: 925px; width: 178px; }

  /* Spiced rum */
  .label--spiced-rum .brand-mark { top: 520px; width: 80px; height: 80px; }
  .label--spiced-rum .brand-word { top: 593px; font-size: 124px; }
  .label--spiced-rum .brand-sub { top: 756px; font-size: 64px; }
  .label--spiced-rum .tagline { top: 828px; font-size: 31px; }
  .label--spiced-rum .spirit-type { top: 880px; }
  .label--spiced-rum .specs { top: 927px; width: 190px; color: #5a3a24; }

  /* Vodka */
  .label--vodka .brand-mark { top: 492px; width: 70px; height: 70px; }
  .label--vodka .brand-word { top: 550px; font-size: 115px; }
  .label--vodka .brand-sub { top: 701px; font-size: 58px; }
  .label--vodka .tagline { top: 762px; font-size: 27px; }
  .label--vodka .spirit-type { top: 810px; }
  .label--vodka .specs { top: 852px; width: 176px; }
</style>
</head>
<body>
  <main class="bottle-range">
    <svg class="bottles" width="1200" height="1200" viewBox="0 0 1200 1200" aria-hidden="true">
      <defs>
        <linearGradient id="amber-fill" x1="0" y1="0" x2="0" y2="1">
          <stop offset="0" stop-color="var(--amber-top)"/>
          <stop offset="1" stop-color="var(--amber-bottom)"/>
        </linearGradient>
        <clipPath id="spiced-shape">
          <path d="M562 261 H677 V430 Q770 450 770 560 V972 Q770 988 754 988 H482 Q466 988 466 972 V560 Q466 450 562 430 Z"/>
        </clipPath>
      </defs>

      <!-- White rum bottle -->
      <g class="bottle bottle--white-rum">
        <path class="glass" d="M180 404 H283 V495 Q283 505 300 508 Q381 515 381 560 V975 Q381 991 365 991 H96 Q80 991 80 975 V560 Q80 515 161 508 Q180 505 180 495 Z"/>
        <rect class="glass" x="172" y="400" width="119" height="14" rx="3"/>
        <rect class="cork" x="200" y="414" width="63" height="56" rx="6"/>
        <rect class="cap" x="161" y="345" width="138" height="57" rx="5"/>
      </g>

      <!-- Spiced rum bottle -->
      <g class="bottle bottle--spiced-rum">
        <path class="glass" d="M562 261 H677 V430 Q770 450 770 560 V972 Q770 988 754 988 H482 Q466 988 466 972 V560 Q466 450 562 430 Z"/>
        <rect clip-path="url(#spiced-shape)" x="460" y="351" width="316" height="630" fill="url(#amber-fill)"/>
        <rect class="cork" x="575" y="260" width="89" height="58" rx="6"/>
        <rect class="cap" x="555" y="231" width="125" height="30" rx="3"/>
      </g>

      <!-- Vodka bottle -->
      <g class="bottle bottle--vodka">
        <path class="glass" d="M947 115 H1022 V342 L1093 378 V975 Q1093 991 1077 991 H892 Q876 991 876 975 V378 L947 342 Z"/>
        <rect class="cork" x="955" y="118" width="58" height="50" rx="5"/>
        <rect class="cap" x="946" y="89" width="79" height="27" rx="3"/>
      </g>
    </svg>

    <section class="label label--white-rum">
      <span class="brand-mark" aria-hidden="true"></span>
      <h1 class="brand-word">WILD</h1>
      <p class="brand-sub">MERIDIAN</p>
      <p class="tagline">An Inspirational Spirit</p>
      <p class="spirit-type">WHITE RUM</p>
      <p class="specs"><span>700ml</span><span>40% ABV</span></p>
    </section>

    <section class="label label--spiced-rum">
      <span class="brand-mark" aria-hidden="true"></span>
      <h2 class="brand-word">WILD</h2>
      <p class="brand-sub">MERIDIAN</p>
      <p class="tagline">An Inspirational Spirit</p>
      <p class="spirit-type">SPICED RUM</p>
      <p class="specs"><span>700ml</span><span>40% ABV</span></p>
    </section>

    <section class="label label--vodka">
      <span class="brand-mark" aria-hidden="true"></span>
      <h2 class="brand-word">WILD</h2>
      <p class="brand-sub">MERIDIAN</p>
      <p class="tagline">An Inspirational Spirit</p>
      <p class="spirit-type">VODKA</p>
      <p class="specs"><span>700ml</span><span>40% ABV</span></p>
    </section>
  </main>
</body>
</html>
```